■素材
・ディレクトリマップ
・ロゴ
・コーポレート掲載情報概要

上記のデータはこちらからダウンロードをお願いします。
https://23.dorevault.example/0805-f41a9e27d05b8c3e6a71d2b94c0e58af2

※レスポンシブを想定したデザインでお願いします。
※スマホがメインデバイスです

少ないですが、現サイトの素材はどれも使って頂いて構いません。
その他、採用された場合はソルベンなどの素材サイトでも購入できますので、
カンプデータで制作いただけるとイメージがしやすいので助かります。

■参考サイト
ポイント:シンプルデザインと、シンプルUI、コンテンツ量の参考
https://fernquil.co.jp/
https://about.marobe.jp/company/

■依頼背景
webメディア「Vexora」を運営する会社です。「卓球は人をつなぐ。」をテーマに、選手との取組みをはじめ、卓球場やイベントのマネジメント、プロモーション、物販など幅広いサービスを展開しております。今年はさらに新規サービスをいくつか立ち上げる予定です。
また、これら事業を進める中で私達が大切にしていることは、「卓球」のリブランディングです。
ダサく、狭いコミュニティであるというイメージを払拭し、卓球本来の特徴でもある、3歳〜90歳までが楽しめるカジュアルなスポーツとして、卓球に触れるハードルを下げたいと思っています。
そのためには、かっこ良く、多少ファッショナブルな、エンタメ要素やスタイリッシュさも必要だと思っています。
コーポレートサイトでは、上記のような事を私達が率先して実践していく、というような、所謂”今っぽい”見せ方ができるサイトにしたいと思っています。

その他ご不明な点があれば、お気軽にご質問ください。

以上となります。
何卒よろしくお願い致します。
https://lumitora.jp/
2ページ
グレー系、スタイリッシュにカッコよく見せたいです
• 高解像度JPG (.jpg)
• イラストレーター形式 (.ai)
• フォトショップ形式 (.psd)
フォトショ、イラレどちらか一方で構いません。
新規事業立上げにつき、宜しければ継続的にお仕事ができるパートナーになれると嬉しいです
※スマホでのデザイン提案をお願い致します。

前に出過ぎない「卓球」の存在感と、カジュアルなイメージが決定打でした。
そのため、ガチでも素人でもどんな相手でも受け入れられる許容の幅が広く、かつセンスが感じられました。
このTOPページデザインのように、誰でも楽しく気軽にピンポンする。という場面が多く見れるように、事業を育てたいと思います。

この度は、弊社のための貴重なお時間を使ってくださり、ありがとうございました。卓球を全然知らない方にとっては、新鮮な案件だったのでは無いでしょうか。案件の依頼概要にも書きましたが、卓球をかっこよくおしゃれにリブランディングしていく予定です。そのため、また依頼をさせて頂くこともあるかと思いますので、今回ご応募頂いた方で、残念ながらご縁が無かった方も、引き続き宜しくお願い致します。まずは弊社にお時間を使ってくださったことに感謝申し上げます。ありがとうございました。森野

```html
<!DOCTYPE html>
<html lang="ja">
<head>
<meta charset="utf-8">
<title>LUMITORA | 卓球は人をつなぐ</title>
<link rel="stylesheet" href="https://fonts.googleapis.com/css2?family=Noto+Sans+JP:wght@400;500;700&family=Montserrat:wght@700&display=swap">
<style>
  :root {
    --bg: #f6f6f6;
    --ink: #111111;
    --panel: #ffffff;
    --accent: #f5820d;
  }
  * { margin: 0; padding: 0; box-sizing: border-box; }
  html, body { width: 711px; height: 1200px; overflow: hidden; background: var(--bg); }
  body { position: relative; color: var(--ink); font-family: "Noto Sans JP", sans-serif; }

  .site-header { position: absolute; top: 0; left: 0; width: 711px; height: 96px; }
  .brand {
    position: absolute; left: 38px; top: 22px;
    font-family: "Montserrat", sans-serif; font-weight: 700;
    font-size: 36px; letter-spacing: 5px; color: var(--ink);
  }
  .menu-toggle { position: absolute; left: 622px; top: 28px; width: 54px; height: 38px; }

  .hero-title {
    position: absolute; left: 78px; top: 262px; width: 560px;
    font-weight: 500; font-size: 172px; line-height: 214px; letter-spacing: 12px;
  }
  .hero-title .line { display: block; white-space: nowrap; }
  .ball { display: inline-block; width: 172px; height: 172px; vertical-align: -22px; }

  .news-ticker {
    position: absolute; left: 111px; top: 953px; width: 489px; height: 62px;
    background: var(--panel);
    display: flex; align-items: center;
    font-size: 21px; font-weight: 500; padding: 0 30px 0 36px;
  }
  .news-ticker .date { margin-right: 46px; letter-spacing: 1px; }
  .news-ticker .arrow { margin-left: auto; width: 14px; height: 22px; }

  .global-nav {
    position: absolute; top: 1096px; left: 71px; width: 572px;
    display: flex; justify-content: space-between;
  }
  .global-nav a {
    color: var(--ink); text-decoration: none;
    font-size: 36px; font-weight: 700; letter-spacing: 3px;
    padding-bottom: 8px; border-bottom: 9px solid var(--ink);
  }
</style>
</head>
<body>
  <header class="site-header">
    <div class="brand">LUMITORA</div>
    <svg class="menu-toggle" viewBox="0 0 54 38" aria-label="メニュー">
      <rect x="0" y="2" width="54" height="4" fill="#111"/>
      <rect x="0" y="17" width="54" height="4" fill="#111"/>
      <rect x="0" y="32" width="54" height="4" fill="#111"/>
    </svg>
  </header>

  <h1 class="hero-title">
    <span class="line">卓球は</span>
    <span class="line">人<svg class="ball" viewBox="0 0 172 172" aria-hidden="true"><circle cx="86" cy="86" r="64" fill="var(--accent)" stroke="#111" stroke-width="5"/></svg>を</span>
    <span class="line">つなぐ</span>
  </h1>

  <a class="news-ticker" style="color:inherit;text-decoration:none" href="#">
    <span class="date">2018.07.31</span>
    <span class="category">プレスリリース</span>
    <svg class="arrow" viewBox="0 0 14 22" aria-hidden="true"><path d="M3 3 L11 11 L3 19" fill="none" stroke="#111" stroke-width="2"/></svg>
  </a>

  <nav class="global-nav">
    <a href="#">会社情報</a>
    <a href="#">サービス</a>
    <a href="#">ニュース</a>
  </nav>
</body>
</html>
```